Quellmoor Medical Center Wall Mural

I need to design a wall mural for an interior wall measuring 3 meters by 20 meters. that includes either all of the services provided or a map of the locations listed on this webpage https://www.quellmoor-medical.org/locations. It just needs to be very creative.

Executives

```html
<!DOCTYPE html>
<html lang="en">
<head>
<meta charset="utf-8">
<title>Quellmoor Medical Center – Services Mural</title>
<link href="https://fonts.googleapis.com/css2?family=Poppins:wght@400;500&display=swap" rel="stylesheet">
<style>
  :root {
    --red: #c8132f;
    --black: #1b1b1e;
    --white: #ffffff;
    --bg-top: #1d4a78;
    --bg-mid: #3a3d6e;
    --bg-bottom: #7a2a5c;
  }
  * { margin: 0; padding: 0; box-sizing: border-box; }
  html, body {
    width: 1200px;
    height: 180px;
    overflow: hidden;
  }
  .mural {
    position: relative;
    width: 1200px;
    height: 180px;
    overflow: hidden;
    font-family: "Poppins", sans-serif;
  }
  .mural__backdrop {
    position: absolute;
    inset: 0;
    background:
      radial-gradient(ellipse at 40% 0%, rgba(60,120,170,0.55), transparent 60%),
      linear-gradient(180deg, var(--bg-top) 0%, var(--bg-mid) 45%, var(--bg-bottom) 100%);
  }
  .services {
    position: absolute;
    left: 7px;
    top: 16.3px;
    display: grid;
    grid-template-columns: 168.6px 182.1px 155.2px 162.1px 182.6px 166.3px 176.1px;
    grid-template-rows: repeat(4, 30.3px);
    grid-auto-flow: column;
    row-gap: 8.8px;
    list-style: none;
  }
  .service {
    display: flex;
    align-items: center;
    padding-left: var(--indent, 19.6px);
    color: var(--white);
    font-size: 12.8px;
    font-weight: 400;
    white-space: nowrap;
    overflow: hidden;
  }
  .service--red { background: var(--red); }
  .service--black { background: var(--black); }

  /* column indents */
  .service:nth-child(n+5):nth-child(-n+8)   { --indent: 21px; }
  .service:nth-child(n+9):nth-child(-n+12)  { --indent: 24px; }
  .service:nth-child(n+13):nth-child(-n+16) { --indent: 24px; }
  .service:nth-child(n+17):nth-child(-n+20) { --indent: 24px; }
  .service:nth-child(n+21):nth-child(-n+24) { --indent: 8px; }
  .service:nth-child(n+25)                  { --indent: 20px; }
</style>
</head>
<body>
<main class="mural">
  <div class="mural__backdrop" role="img" aria-label="Blue to purple backdrop of softly lit hexagonal tiles"></div>
  <ul class="services" aria-label="Quellmoor Medical Center services">
    <li class="service service--red">Cardiac Rehab</li>
    <li class="service service--black">Cardiovascular</li>
    <li class="service service--red">Care Management</li>
    <li class="service service--black">Critical Care Unit</li>

    <li class="service service--black">Dermatology</li>
    <li class="service service--red">Diabetes Care Services</li>
    <li class="service service--black">Emergency Care</li>
    <li class="service service--red">Endocrinology</li>

    <li class="service service--red">Endoscopy</li>
    <li class="service service--black">Family Medicine</li>
    <li class="service service--red">Fitness Center</li>
    <li class="service service--black">Gastroenterology</li>

    <li class="service service--black">General Surgery</li>
    <li class="service service--red">Internal Medicine</li>
    <li class="service service--black">Joint Replacement</li>
    <li class="service service--red">Labor &amp; Delivery</li>

    <li class="service service--red">Laboratory Services</li>
    <li class="service service--black">Medical Care Unit</li>
    <li class="service service--red">Medical Supplies</li>
    <li class="service service--black">Neurology</li>

    <li class="service service--black">Nursing Services</li>
    <li class="service service--red">Nutrition</li>
    <li class="service service--black">Obstetrics/Gynecology</li>
    <li class="service service--red">Occupational Medicine</li>

    <li class="service service--red">Ophthalmology</li>
    <li class="service service--black">Orthopedic Care</li>
    <li class="service service--red">Otolaryngology (ENT)</li>
    <li class="service service--black">And More</li>
  </ul>
</main>
</body>
</html>
```